Letterhead Design Project

Attached is our new Logo and a copy of our old letter head
Looking to rebrand with our new logo

Reason: I want to show a business card design

Industry/Entity Type

Film Production

Colors

Designer to choose colors to be used in the design.

Requirements
Must have
• The information on the old letterhead

```html
<!DOCTYPE html>
<html lang="en">
<head>
<meta charset="utf-8">
<title>Keelo International – Letterhead &amp; Business Card</title>
<link href="https://fonts.googleapis.com/css2?family=Jost:wght@400;500&display=swap" rel="stylesheet">
<style>
  :root {
    --bg: #dcdcd8;
    --paper: #ffffff;
    --card: #f6f6f4;
    --blue: #1f6f9e;
    --orange: #e8761e;
    --ink: #3d3d3d;
    --muted: #7a7a7a;
    --rule: #b8b8b8;
  }
  * { margin: 0; padding: 0; box-sizing: border-box; }
  html, body { width: 1200px; height: 1200px; overflow: hidden; }
  body {
    background: var(--bg);
    font-family: 'Jost', sans-serif;
    color: var(--ink);
    position: relative;
  }
  .brand {
    display: flex;
    align-items: center;
    gap: 10px;
    color: var(--blue);
    font-weight: 500;
    letter-spacing: 0.12em;
    text-transform: uppercase;
    line-height: 1.1;
  }
  .brand-dot {
    width: 14px; height: 14px;
    border-radius: 50%;
    background: var(--orange);
    flex: none;
  }
  .contact-list { list-style: none; }
  .contact-list li {
    display: flex;
    align-items: flex-start;
    gap: 10px;
    text-transform: uppercase;
    letter-spacing: 0.06em;
  }
  .contact-list svg { flex: none; fill: var(--orange); }

  /* Letterhead */
  .letterhead {
    position: absolute;
    left: 460px; top: 100px;
    width: 700px; height: 990px;
    background: var(--paper);
    box-shadow: 0 6px 24px rgba(0,0,0,0.12);
    padding: 70px 60px 50px;
  }
  .letterhead-header {
    display: flex;
    justify-content: space-between;
    align-items: flex-start;
  }
  .letterhead .brand { font-size: 24px; margin-top: 40px; }
  .letterhead .brand-name { display: block; }
  .letterhead .brand-sub { display: block; font-size: 14px; letter-spacing: 0.2em; }
  .letterhead-details { width: 250px; }
  .tagline {
    font-size: 13px;
    text-transform: uppercase;
    letter-spacing: 0.05em;
    line-height: 1.35;
    margin-bottom: 14px;
  }
  .letterhead .contact-list li { font-size: 10.5px; margin-bottom: 7px; }
  .letterhead-footer {
    position: absolute;
    left: 60px; right: 60px; bottom: 50px;
    border-top: 1px solid var(--rule);
    padding-top: 10px;
    font-size: 11px;
    color: var(--muted);
    line-height: 1.6;
  }

  /* Business card */
  .business-card {
    position: absolute;
    left: 40px; top: 830px;
    width: 390px; height: 226px;
    background: var(--card);
    box-shadow: 0 6px 18px rgba(0,0,0,0.14);
    display: flex;
    align-items: center;
    padding: 0 28px;
    gap: 26px;
  }
  .business-card .brand { font-size: 17px; width: 170px; }
  .business-card .brand-sub { display: block; font-size: 11px; letter-spacing: 0.18em; }
  .card-name {
    font-size: 15px;
    letter-spacing: 0.1em;
    text-transform: uppercase;
    margin-bottom: 12px;
  }
  .business-card .contact-list li { font-size: 8.5px; margin-bottom: 8px; line-height: 1.4; }
</style>
</head>
<body>

<section class="letterhead">
  <header class="letterhead-header">
    <div class="brand">
      <span class="brand-dot"></span>
      <span><span class="brand-name">Keelo</span><span class="brand-sub">International</span></span>
    </div>
    <div class="letterhead-details">
      <p class="tagline">Supply &amp; Management of<br>Infrastructure &amp; Logistics</p>
      <ul class="contact-list">
        <li>
          <svg width="11" height="11" viewBox="0 0 24 24"><path d="M6.6 10.8a15 15 0 0 0 6.6 6.6l2.2-2.2a1 1 0 0 1 1-.25 11.4 11.4 0 0 0 3.6.57 1 1 0 0 1 1 1V20a1 1 0 0 1-1 1A17 17 0 0 1 3 4a1 1 0 0 1 1-1h3.5a1 1 0 0 1 1 1c0 1.25.2 2.45.57 3.57a1 1 0 0 1-.25 1z"/></svg>
          <span>Ph. 0400 123 456</span>
        </li>
        <li>
          <svg width="11" height="11" viewBox="0 0 24 24"><path d="M2 5h20v14H2z M2 5l10 7 10-7" /></svg>
          <span>hello@keelo.com.au</span>
        </li>
        <li>
          <svg width="11" height="11" viewBox="0 0 24 24"><path d="M12 2a7 7 0 0 0-7 7c0 5 7 13 7 13s7-8 7-13a7 7 0 0 0-7-7zm0 9.5A2.5 2.5 0 1 1 12 6.5a2.5 2.5 0 0 1 0 5z"/></svg>
          <span>P.O. Box 210 Fernvale QLD 4306<br>P.O. Box 380 Moorebank NSW 2172</span>
        </li>
      </ul>
    </div>
  </header>

  <footer class="letterhead-footer">
    <p>KEELO Film Services | KEELO Pilot Escorts | KEELO Tour Management | KEELO Driver are divisions of KEELO International Pty Ltd</p>
    <p>ACN 204 518 377 ABN 31 204 518 377</p>
  </footer>
</section>

<section class="business-card">
  <div class="brand">
    <span class="brand-dot"></span>
    <span><span class="brand-name">Keelo</span><span class="brand-sub">International</span></span>
  </div>
  <div class="card-details">
    <p class="card-name">Dean Harlow</p>
    <ul class="contact-list">
      <li>
        <svg width="9" height="9" viewBox="0 0 24 24"><path d="M6.6 10.8a15 15 0 0 0 6.6 6.6l2.2-2.2a1 1 0 0 1 1-.25 11.4 11.4 0 0 0 3.6.57 1 1 0 0 1 1 1V20a1 1 0 0 1-1 1A17 17 0 0 1 3 4a1 1 0 0 1 1-1h3.5a1 1 0 0 1 1 1c0 1.25.2 2.45.57 3.57a1 1 0 0 1-.25 1z"/></svg>
        <span>+61 400123456</span>
      </li>
      <li>
        <svg width="9" height="9" viewBox="0 0 24 24"><path d="M2 5h20v14H2z M2 5l10 7 10-7" /></svg>
        <span>dean@keelo.com.au</span>
      </li>
      <li>
        <svg width="9" height="9" viewBox="0 0 24 24"><path d="M12 2a7 7 0 0 0-7 7c0 5 7 13 7 13s7-8 7-13a7 7 0 0 0-7-7zm0 9.5A2.5 2.5 0 1 1 12 6.5a2.5 2.5 0 0 1 0 5z"/></svg>
        <span>P.O. Box 210<br>Fernvale QLD 4306</span>
      </li>
    </ul>
  </div>
</section>

</body>
</html>
```